Website Design - for Energy Efficiency company - large corporate feel

Hi there,
Thanks for checking out this project!
We're a UK based energy efficiency business. We arrange for energy efficient systems to be fitted in people's houses (i.e. efficient boilers, solar panels etc.) However, we do not install them ourselves as we have accredited installers who install on our behalf. Therefore the website should appeal to these businesses and have a very professional corporate feel. The final design should communicate that we are a financially safe large corporation.
Our existing website should not be used for inspiration as the style and content are very outdated (it was from a time when were installers - which we no longer are).
The new website design should use the greens from our logo, however I don't want the site saturated in this colour.
I'm really open to your chosen layout and therefore I'm not a huge fan of including links to websites I like - as I don't want to limit your own creativity. However, I would like it to look corporate (but not too boring and unimaginative).
So here's a few links to websites that I feel give a feel of financially safe / large corporate etc. Although you certainly don't have to design with this style / layout in mind:
http://www.brenholt.org.uk/advice
http://www.tavishworks.co.uk/
http://www.dqvb.org.uk/
http://www.orrinlodgeway.co.uk/
http://www.pkwynd.co.uk/ (very bad design but looks corporate)
http://www.ferrowmoor.org.uk/
http://www.tq.co.uk/ (looks corporate but too busy and boring)
http://www.quellaro.co.uk/business/index.htm
http://www.mobrevo.com/
https://www.tervold.com/en/index.html
The site is for 4 different audiences:
Consumers | Businesses | Public Sector | Installers
Therefore, it's important that there is some form of way of splitting the site up into these sections (almost like 4 websites in 1). Each section will then have the navigation menu with 7 links.
I've attached our logo (company-logo.jpg) and another logo design we have to display inline with regulations (fair-loan-logo.jpg).
Happy designing, and thank you!

```html
<!DOCTYPE html>
<html lang="en">
<head>
<meta charset="utf-8">
<title>Verdant Hearth Energy</title>
<link href="https://fonts.googleapis.com/css2?family=Ubuntu:wght@300;400;500;700&family=Arimo:wght@400&display=swap" rel="stylesheet">
<style>
:root{
  --green:#5e9a1f;
  --green-dark:#4b7f14;
  --lime:#c7d81b;
  --ink:#1b1b1b;
  --text:#333;
  --muted:#666;
  --navy:#1d3557;
  --rule:#c9c9c9;
  --panel:#ebebeb;
  --tab:#e2e2e2;
  --footer:#2b2b2b;
}
*{box-sizing:border-box;margin:0;padding:0}
html,body{width:899px;height:1200px;overflow:hidden;background:#fff}
body{position:relative;font-family:'Ubuntu',sans-serif;color:var(--text)}
.abs{position:absolute}
a{color:inherit;text-decoration:none}

.topbar{left:0;top:0;width:899px;height:26px;background:#e6e6e6;font-size:10px;color:var(--ink)}
.topbar nav{position:absolute;left:436px;top:7px;display:flex;gap:9px}
.topbar nav a:first-child{font-weight:700}
.flags{position:absolute;left:754px;top:6px;display:flex;gap:3px}
.flags span{width:20px;height:13px;background:#2c3f8c;border:1px solid #999}
.flags span:last-child{background:linear-gradient(#b22 0 50%,#fff 50% 100%)}

.brand{left:77px;top:52px;display:flex;align-items:center;gap:8px}
.brand .mark{width:34px;height:34px;border-radius:50%;background:var(--green)}
.brand .name{font-size:26px;font-weight:500;color:var(--green);letter-spacing:-.3px}

.social{left:749px;top:56px;display:flex;gap:5px}
.social span{width:20px;height:20px;border-radius:50%;background:var(--navy)}
.callfree{right:78px;top:80px;font-size:19px;font-weight:300;color:var(--navy)}
.callfree b{font-weight:700}

.mainnav{left:0;top:122px;width:899px;height:31px;background:#000}
.mainnav ul{list-style:none;display:flex;position:absolute;left:76px;top:10px;font-size:10.5px;color:#fff}
.mainnav li{margin-right:26px}
.mainnav li:not(:last-child)::after{content:".";margin-left:26px}
.getintouch{left:643px;top:122px;width:256px;height:31px;background:var(--lime);color:#fff;font-weight:700;font-size:14px;padding:6px 0 0 9px}

.hero{left:0;top:164px;width:899px;height:312px;background:linear-gradient(#a9c3d8 0%,#cbd8dc 40%,#b4b98a 58%,#8a9a4a 78%,#4f6a2e 100%)}
.arrow{top:389px;width:44px;height:44px}
.arrow.prev{left:16px}.arrow.next{left:829px}
.heroshade{left:0;top:476px;width:899px;height:14px;background:linear-gradient(90deg,#fff,#aaa 40%,#222 100%);clip-path:polygon(0 0,100% 0,100% 60%,0 10%)}

.intro{left:0;top:497px;width:899px;text-align:center}
.intro h1{font-size:14.5px;font-weight:700;color:var(--green);letter-spacing:.3px}
.intro p{font-size:13px;color:var(--muted);line-height:15.5px;margin-top:5px;letter-spacing:.3px}
.dotted{left:0;width:899px;border-top:1px dotted #999}

.datebadge{left:77px;top:585px;width:41px;height:58px;background:#777;color:#fff;text-align:center;font-size:11px;line-height:13px;padding-top:5px;clip-path:polygon(0 0,100% 0,100% 100%,50% 85%,0 100%)}
.datebadge b{display:block;font-size:14px;font-weight:400}
.posthead{left:124px;top:585px;width:446px;height:32px;border:1px solid #999;display:flex;align-items:center;gap:5px;padding-left:3px}
.posthead .avatar{width:24px;height:24px;background:#c89a7a;border:1px solid #999}
.posthead strong{display:block;font-size:9.5px;color:#000}
.posthead small{font-size:9.5px;color:var(--green)}
.posthead small em{font-style:normal;color:#777;font-weight:500}
.postbody{left:127px;top:624px;width:448px;font-size:8.7px;line-height:15.2px;color:#444}
.continue{left:130px;top:726px;font-size:8.7px;font-weight:500;color:#222}

.enews{left:584px;top:585px;width:238px;height:33px;background:linear-gradient(#3a3a3a,#111);color:#fff;font-size:12.5px;font-weight:700;display:flex;align-items:center;gap:10px;padding-left:6px}
.enews .icon{width:24px;height:20px;background:#ccd;border-radius:2px}
.enews em{font-family:Georgia,serif;font-size:11px}
.event{left:589px;width:237px;height:62px;border-bottom:1px solid #999;font-size:9.5px;line-height:15.5px;color:#222;padding-left:20px}
.event .num{position:absolute;left:0;top:3px;width:15px;height:20px;border:1.5px solid #222;border-radius:2px;font-size:10px;text-align:center;line-height:17px}
.event h3{font-size:10.5px;font-weight:500;color:var(--green)}

.tabs{left:76px;top:798px;display:flex;gap:3px}
.tabs span{height:33px;background:var(--tab);border:1px solid #ccc;border-bottom:none;font-size:14px;font-weight:500;color:#222;display:flex;align-items:center;justify-content:center}
.tabs .active{background:#f2f2f2;color:#555}
.panel{left:76px;top:831px;width:746px;height:217px;background:linear-gradient(#f0f0f0,#e6e6e6);border:1px solid #ccc}
.badge{left:78px;top:846px;width:44px;height:60px;background:var(--green-dark);border-radius:3px}
.panel h2{position:absolute;left:53px;top:15px;font-size:15px;font-weight:500;color:#333;line-height:17px;width:196px;border-bottom:1px solid #ccc;padding-bottom:2px}
.panel .lede{position:absolute;left:54px;top:59px;width:450px;font-size:8.7px;line-height:15.2px;color:#333}
.panel h4{position:absolute;left:23px;top:109px;font-size:13px;font-weight:400;color:#444}
.panel ul{position:absolute;left:24px;top:131px;list-style:none;font-family:'Arimo',Arial,sans-serif;font-size:8px;line-height:14.7px}
.panel li::before{content:"\27A4";color:var(--green);margin-right:7px;font-size:6px}
.panel li a{color:var(--green-dark);text-decoration:underline}
.pager{top:203px;width:15px;height:7px;border:1px solid #bbb;background:#f7f7f7}
.portrait{left:556px;top:831px;width:266px;height:217px;background:linear-gradient(90deg,rgba(230,230,230,0),#c9a28a 35%,#8197b0 75%,#6f8aa8)}

.companies h2{position:absolute;left:77px;top:1066px;font-size:14px;font-weight:500;color:#444}
.partners{left:112px;top:1098px;display:flex;gap:14px;align-items:center;font-size:16px;font-weight:300;color:#888}
.partners span{display:flex;align-items:center;gap:3px}
.partners i{width:14px;height:14px;background:#aaa;display:inline-block}

.footer{left:0;top:1136px;width:899px;height:64px;background:linear-gradient(#222,#3a3a3a);color:#fff;font-family:Arial,sans-serif;font-size:9.5px}
.footer nav{position:absolute;left:77px;top:18px;display:flex}
.footer nav a:not(:last-child)::after{content:"|";margin:0 16px}
.footer p{position:absolute;left:77px;top:40px}
</style>
</head>
<body>

<header>
  <div class="abs topbar">
    <nav><a href="#">For Home</a><a href="#">For Business</a><a href="#">For Public Sector</a><a href="#">About</a><a href="#">Global sites</a></nav>
    <div class="flags"><span></span><span></span><span></span></div>
  </div>
  <div class="abs brand"><span class="mark"></span><span class="name">Verdant Hearth Energy</span></div>
  <div class="abs social"><span></span><span></span><span></span></div>
  <div class="abs callfree">Call free on <b>0800 555 0192</b></div>
  <nav class="abs mainnav">
    <ul><li>HOME</li><li>ABOUT US</li><li>ENERGY</li><li>WHAT WE DO</li><li>NEWS</li><li>CONTACT US</li></ul>
  </nav>
  <div class="abs getintouch">Get in touch with us &#8964;</div>
</header>

<section>
  <div class="abs hero" role="img" aria-label="Wind turbines standing across green farmland under a pale sky"></div>
  <svg class="abs arrow prev" viewBox="0 0 44 44"><circle cx="22" cy="22" r="20" fill="none" stroke="#fff" stroke-width="2"/><path d="M25 13l-9 9 9 9" fill="none" stroke="#fff" stroke-width="2.5"/></svg>
  <svg class="abs arrow next" viewBox="0 0 44 44"><circle cx="22" cy="22" r="20" fill="none" stroke="#fff" stroke-width="2"/><path d="M19 13l9 9-9 9" fill="none" stroke="#fff" stroke-width="2.5"/></svg>
  <div class="abs heroshade"></div>
  <div class="abs intro">
    <h1>PRAESENT VESTIBULUM MOLESTIE LACUS. AENEAN NONUMMY HENDRERIT MAURIS. PHASELLUS</h1>
    <p>Praesent vestibulum molestie lacus. Aenean nonummy hendrerit mauris. Phasellus porta.<br>Fusce suscipit varius mi. Cum sociis natoque penatibus.</p>
  </div>
  <div class="abs dotted" style="top:556px"></div>
</section>

<section>
  <div class="abs datebadge"><b>17</b>Oct</div>
  <div class="abs posthead">
    <span class="avatar" role="img" aria-label="Author portrait"></span>
    <div><strong>Praesent vestibulum molestie lacus. Aenean nonummy hendrerit mauris. Phasellus</strong><small>By Mara Tilden &gt; <em>Media</em></small></div>
  </div>
  <p class="abs postbody">simply dummy text of the printing and typesetting industry. Lorem Ipsum has been the industry's standard when an un known printer took a galley.Aenean nonummy hendrerit mauris. Phasellus porta. Fusce suscipit varius mi. Cum sociis natoque penatibus et magnis dis parturient montes, nascetur ridiculus. simply dummy text of the printing and typesetting industry. Lorem Ipsum has been the industry's standard when an un known printer took a galley.Aenean nonummy hendrerit mauris. Phasellus porta. Fusce suscipit varius mi. Cum sociis natoque penatibus et magnis dis parturient montes, nascetur ridiculus.</p>
  <a class="abs continue" href="#">Continue Reading</a>

  <div class="abs enews"><span class="icon"></span><span>SIGN UP <em>for</em> ENEWS</span></div>
  <div class="abs event" style="top:627px"><span class="num">1</span><h3>Impact of the Carbon Price &amp; Carbon</h3>Thursday 10 November - Afternoon Conference.<br>Registration fee includes lunch.</div>
  <div class="abs event" style="top:689px"><span class="num">2</span><h3>Impact of the Carbon Price &amp; Carbon</h3>Thursday 10 November - Afternoon Conference.<br>Registration fee includes lunch.</div>
  <div class="abs dotted" style="top:766px"></div>
</section>

<section>
  <div class="abs tabs">
    <span class="active" style="width:112px">Consumers</span>
    <span style="width:130px">Businesses</span>
    <span style="width:130px">Public Sector</span>
    <span style="width:130px">Installers</span>
  </div>
  <div class="abs panel">
    <h2>Everything About Consumers</h2>
    <p class="lede">simply dummy text of the printing and typesetting industry. Lorem Ipsum has been the industry's standard when an un known printer took a galley.Aenean nonummy hendrerit mauris. Phasellus porta. Fusce suscipit varius mi. Cum sociis natoque penatibus et magnis dis parturient montes, nascetur ridiculus.</p>
    <h4>View Categories</h4>
    <ul>
      <li><a href="#">Lorem ipsum dolor sit</a></li>
      <li><a href="#">Lorem ipsum dolor sit</a></li>
      <li><a href="#">Lorem ipsum dolor sit</a></li>
      <li><a href="#">Lorem ipsum dolor sit</a></li>
    </ul>
    <span class="abs pager" style="left:22px"></span>
    <span class="abs pager" style="left:282px"></span>
  </div>
  <div class="abs badge" role="img" aria-label="Approved provider badge"></div>
  <div class="abs portrait" role="img" aria-label="Businessman in a suit, thinking, hand at his temple"></div>
</section>

<section class="companies">
  <h2>Our Companies</h2>
  <div class="abs partners">
    <span><i></i>brightmill</span>
    <span><i></i>sonarleaf</span>
    <span><i></i>plotharbor</span>
    <span><i></i>scriptvale</span>
    <span><i></i>meshcove</span>
    <span><i></i>framenest</span>
  </div>
</section>

<footer class="abs footer">
  <nav><a href="#">Home</a><a href="#">About</a><a href="#">Teams</a><a href="#">Energy</a><a href="#">News</a><a href="#">What We Do</a><a href="#">Register</a><a href="#">Contact Us</a></nav>
  <p>Copyright © 2007 - 2013 - verdanthearth. - All Rights Reserved</p>
</footer>

</body>
</html>
```